2026 Varnex Loprin LWB Vehicle Wrap Design for Ridgeway Electrical and Refrigeration Work Vans

We are Ridgeway Electrical and Refrigeration — a Perth-based commercial electrical, air conditioning and refrigeration company. We service commercial buildings, homes and luxury residential jobs across the metro area and remote WA.
We need a clean, professional and high-impact full vehicle wrap design for our work vans. The vans are our mobile billboards, so the design needs to look sharp from a distance, communicate trust and competence, and clearly show what we do.
Must include:

Our company name: Ridgeway Electrical and Refrigeration
Tagline options (you can choose the strongest placement or suggest alternatives):
“Electrical | Air Conditioning | Refrigeration – Perth & Remote WA”
Licence numbers "AU051237 and EC24813"
Phone number: 0491 538 214
Website: ridgewayelectricalrefrigeration.com.au
Email: admin@ridgewayelectricalrefrigeration.com.au
Our existing logo (will be uploaded)

Style we want:

Professional, modern and trustworthy
Bold enough to stand out on the road but not flashy or overly busy
Clean hierarchy so the company name and phone number are readable at speed
Strong use of contrast

Colour preferences:

Prefer designs that work with our existing branding (we will upload the logo and brand colours)
Open to strong, professional colour combinations (navy/dark blue, black, white, and one accent colour such as orange, red or electric blue often work well in the trades)

Avoid:

Cluttered designs with too much text
Cartoonish or overly “tradie” looking graphics
Designs that look cheap or dated

Additional notes:

Design should scale well so we can use the same concept across multiple vans
We will need print-ready files (high-res, layered) at the end

Please upload your best concepts. We will give clear feedback and work with the winning designer to refine the final artwork for production.

Target Market(s)

commercial buildings, homes and luxury residential jobs across the metro area and remote WA.

Industry/Entity Type

Electrical, Air Conditioning and Refrigeration

Colors
0054AA
0677BA
7BADD7
CADEEF
E8F1F8

Requirements
Must have
• Our company name: Ridgeway Electrical and Refrigeration Tagline options (you can choose the strongest placement or suggest alternatives): “Electrical | Air Conditioning | Refrigeration – Perth & Remote WA” Licence numbers "AU051237 and EC24813" Phone number: 0491 538 214 Website: ridgewayelectricalrefrigeration.com.au Email: admin@ridgewayelectricalrefrigeration.com.au Our existing logo (will be uploaded)
Nice to have
• Professional, modern and trustworthy Bold enough to stand out on the road but not flashy or overly busy Clean hierarchy so the company name and phone number are readable at speed Strong use of contrast
Should not have
• Cluttered designs with too much text Cartoonish or overly “tradie” looking graphics Designs that look cheap or dated

```html
<!DOCTYPE html>
<html lang="en">
<head>
<meta charset="utf-8">
<title>Ridgeway Electrical and Refrigeration – Van Wrap Side Panel</title>
<link rel="stylesheet" href="https://fonts.googleapis.com/css2?family=Montserrat:wght@600;700&display=swap">
<style>
  :root {
    --brand-navy: #0054AA;
    --brand-blue: #0677BA;
    --brand-sky: #7BADD7;
    --brand-mist: #CADEEF;
    --brand-ice: #E8F1F8;
    --wrap-white: #FFFFFF;
    --page-bg: #FFFFFF;
    --text-light: #EEF3F8;
  }
  html, body {
    margin: 0;
    padding: 0;
    width: 1200px;
    height: 675px;
    overflow: hidden;
    background: var(--page-bg);
  }
  .wrap-canvas {
    display: block;
    width: 1200px;
    height: 675px;
    font-family: "Montserrat", sans-serif;
  }
  .panel-outline { fill: var(--wrap-white); stroke: var(--brand-mist); stroke-width: 1; }
  .panel-blue { fill: var(--brand-blue); }
  .panel-fade { fill: var(--brand-sky); opacity: 0.55; }
  .chevron-light { fill: var(--brand-mist); opacity: 0.35; }
  .chevron-deep { fill: var(--brand-navy); opacity: 0.25; }
  .service-tab { fill: var(--brand-sky); opacity: 0.7; }
  .service-text { fill: var(--wrap-white); font-weight: 700; font-size: 14.5px; }
  .licence-text { fill: var(--text-light); font-weight: 600; font-size: 13px; }
  .brand-square { fill: var(--brand-navy); }
  .brand-name { fill: var(--text-light); font-weight: 700; font-size: 31px; letter-spacing: 0.5px; }
  .email-band { fill: var(--brand-mist); opacity: 0.8; }
  .email-text { fill: var(--brand-navy); font-weight: 700; font-size: 9.6px; }
  .phone-band { fill: var(--brand-navy); }
  .phone-text { fill: var(--wrap-white); font-weight: 700; font-size: 24px; }
  .web-text { fill: var(--brand-navy); font-weight: 700; font-size: 8.6px; }
</style>
</head>
<body>
<svg class="wrap-canvas" viewBox="0 0 1200 675" xmlns="http://www.w3.org/2000/svg">
  <!-- side panel artboard -->
  <rect class="panel-outline" x="128" y="128" width="902" height="312" rx="18"/>

  <!-- blue field with right-pointing chevron edge -->
  <path class="panel-blue" d="M146 128 H700 L700 128 L756 300 L672 440 H146 Q128 440 128 422 V146 Q128 128 146 128 Z"/>
  <path class="panel-fade" d="M146 128 H360 L262 226 L380 300 L200 440 H146 Q128 440 128 422 V146 Q128 128 146 128 Z"/>

  <!-- layered chevrons -->
  <path class="chevron-light" d="M262 226 L360 150 L600 150 L500 226 Z"/>
  <path class="chevron-deep" d="M330 300 L520 210 L640 300 L520 390 Z"/>

  <!-- services list -->
  <rect class="service-tab" x="166" y="144" width="166" height="18"/>
  <text class="service-text" x="168" y="158">AIR CONDITIONING</text>
  <rect class="service-tab" x="166" y="165" width="122" height="18"/>
  <text class="service-text" x="168" y="179">REFRIGERATION</text>
  <rect class="service-tab" x="168" y="186" width="92" height="18"/>
  <text class="service-text" x="170" y="200">ELECTRICAL</text>

  <!-- licence numbers -->
  <text class="licence-text" x="170" y="354">EC24813</text>
  <text class="licence-text" x="152" y="372">AU051237</text>

  <!-- brand block -->
  <rect class="brand-square" x="391" y="134" width="166" height="166" rx="6"/>
  <text class="brand-name" x="391" y="336">RIDGEWAY</text>
  <text class="brand-name" x="391" y="368">ELECTRICAL &amp;</text>
  <text class="brand-name" x="391" y="400">REFRIGERATION</text>

  <!-- email -->
  <path class="email-band" d="M389 411 H652 L640 427 H389 Z"/>
  <text class="email-text" x="392" y="422.5">ADMIN@RIDGEWAYELECTRICALREFRIGERATION.COM.AU</text>

  <!-- phone and website -->
  <path class="phone-band" d="M748 285 H958 L948 306 H730 Z"/>
  <text class="phone-text" x="756" y="304">0491 538 214</text>
  <text class="web-text" x="756" y="318">RIDGEWAYELECTRICALREFRIGERATION.COM.AU</text>
</svg>
</body>
</html>
```